New website for concierge mobile medical service

new website for business:
WEBSITE REQUEST LIST:
Luxury product look.
Professional. Clean & simple, NO stock people photos. Graphics OK.
Black and white text.

```html
<!DOCTYPE html>
<html lang="en">
<head>
<meta charset="utf-8">
<title>About Lumen Care</title>
<link rel="stylesheet" href="https://fonts.googleapis.com/css2?family=Lato:wght@400;700&family=Source+Sans+3:wght@600;700&display=swap">
<style>
  :root {
    --ink: #1c1c1c;
    --navy: #062f4d;
    --navy-deep: #020b12;
    --accent: #5b5ba8;
    --heading: #3f51a0;
    --teal-light: #8bd0d8;
    --footer: #1e1e1e;
    --white: #ffffff;
  }
  * { margin: 0; padding: 0; box-sizing: border-box; }
  html, body { width: 1167px; height: 1200px; overflow: hidden; background: var(--white); }
  body { position: relative; font-family: "Lato", sans-serif; color: var(--ink); }

  .site-header { position: absolute; left: 0; top: 0; width: 1167px; height: 104px; background: var(--white); }
  .brand { position: absolute; left: 152px; top: 36px; display: flex; align-items: center; gap: 10px; }
  .brand-dot { width: 26px; height: 26px; border-radius: 50%; background: var(--navy); display: block; }
  .brand-name { font-family: "Lato", sans-serif; font-weight: 700; font-size: 22px; color: var(--navy); white-space: nowrap; }
  .phone { position: absolute; left: 863px; top: 15px; display: flex; align-items: center; gap: 12px; }
  .phone-icon { width: 31px; height: 31px; background: var(--accent); border-radius: 2px; display: flex; align-items: center; justify-content: center; }
  .phone-number { font-weight: 700; font-size: 19px; color: var(--accent); }
  .main-nav { position: absolute; top: 74px; left: 0; width: 100%; }
  .main-nav a { position: absolute; font-weight: 700; font-size: 12px; color: var(--ink); text-decoration: none; white-space: nowrap; }
  .main-nav a.is-active { color: var(--accent); }
  .nav-indicator { position: absolute; left: 867px; top: 99px; width: 64px; height: 5px; background: var(--navy); }

  .hero { position: absolute; left: 0; top: 104px; width: 1167px; height: 257px;
    background: linear-gradient(90deg, var(--navy-deep) 0%, #06263d 40%, var(--navy) 100%); }
  .hero-title { position: absolute; left: 139px; top: 100px; font-family: "Source Sans 3", sans-serif; font-weight: 700; font-size: 46px; color: var(--white); line-height: 1; }
  .hero-graphic { position: absolute; left: 842px; top: 30px; width: 198px; height: 198px; border-radius: 50%;
    border: 3px solid #6fb5e0; background: radial-gradient(circle, #0b4a70 0%, #063656 100%); }

  .about { position: absolute; left: 141px; top: 410px; width: 880px; }
  .about p { font-size: 14.5px; line-height: 22.6px; }
  .about h2 { font-family: "Source Sans 3", sans-serif; font-weight: 600; font-size: 20px; color: var(--heading); line-height: 1; }
  .intro { position: absolute; top: 0; white-space: nowrap; }
  .block { position: absolute; left: 0; width: 880px; }
  .block p { margin-top: 11px; }

  .subscribe { position: absolute; left: 0; top: 824px; width: 1167px; height: 245px;
    background: linear-gradient(135deg, #1b8aa6 0%, #1a7d9d 50%, #1988aa 100%); }
  .subscribe h2 { position: absolute; top: 42px; width: 100%; text-align: center; font-family: "Source Sans 3", sans-serif; font-weight: 600; font-size: 32px; color: var(--white); letter-spacing: 0.5px; }
  .field { position: absolute; top: 100px; width: 309px; height: 43px; background: var(--white); border: 0; padding-left: 15px; font-family: "Lato", sans-serif; font-size: 12px; color: var(--ink); }
  .field::placeholder { color: var(--ink); }
  .field-name { left: 268px; }
  .field-email { left: 590px; }
  .subscribe-btn { position: absolute; left: 268px; top: 152px; width: 631px; height: 43px; border: 0; background: var(--teal-light);
    font-family: "Lato", sans-serif; font-weight: 700; font-size: 15.5px; color: var(--white); }

  .site-footer { position: absolute; left: 0; top: 1069px; width: 1167px; height: 131px; background: var(--footer); color: var(--white); }
  .footer-nav a { position: absolute; top: 23px; font-weight: 700; font-size: 12px; color: var(--white); text-decoration: none; white-space: nowrap; }
  .copyright { position: absolute; top: 56px; width: 100%; text-align: center; font-size: 11px; }
  .social { position: absolute; top: 86px; left: 508px; display: flex; gap: 17px; }
  .social span { width: 16px; height: 16px; border-radius: 50%; background: var(--white); display: block; }
</style>
</head>
<body>
  <header class="site-header">
    <div class="brand"><span class="brand-dot"></span><span class="brand-name">Lumen Care</span></div>
    <div class="phone">
      <span class="phone-icon">
        <svg width="15" height="15" viewBox="0 0 24 24"><path fill="#fff" d="M6.6 10.8c1.4 2.8 3.8 5.1 6.6 6.6l2.2-2.2c.3-.3.7-.4 1-.2 1.1.4 2.3.6 3.6.6.6 0 1 .4 1 1V20c0 .6-.4 1-1 1C10.6 21 3 13.4 3 4c0-.6.4-1 1-1h3.5c.6 0 1 .4 1 1 0 1.3.2 2.5.6 3.6.1.3 0 .7-.2 1L6.6 10.8z"/></svg>
      </span>
      <span class="phone-number">555-010-0199</span>
    </div>
    <nav class="main-nav">
      <a href="#" style="left:384px">HOME</a>
      <a href="#" style="left:461px">ABOUT US</a>
      <a href="#" style="left:563px">WHY LUMEN?</a>
      <a href="#" style="left:676px">SERVICE AREA</a>
      <a href="#" style="left:803px">OTHER</a>
      <a href="#" class="is-active" style="left:885px">FAQ</a>
      <a href="#" style="left:948px">CONTACT US</a>
    </nav>
    <span class="nav-indicator"></span>
  </header>

  <section class="hero">
    <h1 class="hero-title">About Lumen Care</h1>
    <div class="hero-graphic" role="img" aria-label="Line illustration of a car with a medical symbol above it inside a glowing ring"></div>
  </section>

  <main class="about">
    <p class="intro">Dr. Alan Brooks &amp; Dr. Sam Ortega founded Lumen Care and are committed to their mission, vision and values.</p>
    <div class="block" style="top:63px">
      <h2>Our Mission</h2>
      <p>To simplify our patients’ access to quality medical care and help our patients achieve optimal wellness.</p>
    </div>
    <div class="block" style="top:149px">
      <h2>Our Vision</h2>
      <p>Dr. Alan Brooks and Dr Sam Ortega founded Lumen Care with the goal of getting back to the basics: brining the doctor to the patient. We use the latest technology and advancements in medical equipment, electronic records, geo-mapping, and fleet management. We stay on the cutting edge of personalized medical delivery.</p>
    </div>
    <div class="block" style="top:272px">
      <h2>Our Values</h2>
      <p>Treating patients like people, not numbers. Taking time to care and know our patients. Helping our patients achieve optimal wellness through compassionate and comfortable care.</p>
    </div>
  </main>

  <section class="subscribe">
    <h2>Subscribe</h2>
    <input class="field field-name" type="text" placeholder="Enter Name">
    <input class="field field-email" type="email" placeholder="Enter Email Address">
    <button class="subscribe-btn">SUBSCRIBE NOW</button>
  </section>

  <footer class="site-footer">
    <nav class="footer-nav">
      <a href="#" style="left:293px">HOME</a>
      <a href="#" style="left:371px">ABOUT US</a>
      <a href="#" style="left:473px">WHY LUMEN?</a>
      <a href="#" style="left:586px">SERVICE AREA</a>
      <a href="#" style="left:713px">OTHER</a>
      <a href="#" style="left:794px">CONTACT US</a>
    </nav>
    <p class="copyright">Copyright &nbsp;© 2019. &nbsp;Company Name &nbsp;All Rights Reserved</p>
    <div class="social" aria-label="Social links">
      <span></span><span></span><span></span><span></span><span></span>
    </div>
  </footer>
</body>
</html>
```